Hypnosis signage

I need a signage 3.50 mt width x 1.60 length.
I'm attaching a signage.
But few changes the Text in the center slightly out of balance.
I'm attaching also photos that can go in one corner.
Please do keep the color orange
Updates

Please I need the signage in Arial Fonts with colors Orange and Black & White for letters or combination
is up to You .

Thank You
Dorian

Colors
f37022

Requirements
Must have
• Clinical Hypnosis
- Weight Loss
- Fear of
Public Speaking
- Anxiety
- Depression
- PTS
- Stop Smoking
- Confidence Building
- Alcohol Moderation

Book now: www.calmtidetrance.net
or call 9462 3089
Should not have
• do You guys see the letters on the signage? "Harbor Sparrows" if You can do the that with Weight Loss ,Stop Smoking, Fear Of Public Speaking , Alcohol Moderation . The letters a bit out of balance .

```html
<!DOCTYPE html>
<html lang="en">
<head>
<meta charset="utf-8">
<title>Clinical Hypnosis Signage</title>
<link href="https://fonts.googleapis.com/css2?family=Montserrat:wght@400;500;600&display=swap" rel="stylesheet">
<style>
  :root {
    --orange: #f37022;
    --black: #231f20;
    --white: #ffffff;
    --backdrop: #ecebea;
  }
  * { margin: 0; padding: 0; box-sizing: border-box; }
  html, body {
    width: 1200px;
    height: 900px;
    overflow: hidden;
    background: var(--backdrop);
    font-family: "Montserrat", Arial, sans-serif;
  }
  .sign {
    position: absolute;
    left: 40px;
    top: 235px;
    width: 1120px;
    height: 430px;
    overflow: hidden;
    box-shadow: 0 6px 18px rgba(0,0,0,0.25);
  }
  .sign-art {
    position: absolute;
    inset: 0;
    width: 100%;
    height: 100%;
  }
  .title {
    position: absolute;
    right: 52px;
    top: 66px;
    color: var(--orange);
    font-weight: 600;
    font-size: 50px;
    line-height: 1.12;
    text-align: center;
  }
  .services {
    position: absolute;
    list-style: none;
    color: var(--white);
    font-size: 19px;
    font-weight: 400;
    letter-spacing: 0.3px;
  }
  .services li { height: 30px; line-height: 30px; }
  .services li::before { content: "\2022"; margin-right: 5px; }
  .services-left { left: 555px; top: 220px; }
  .services-right { left: 826px; top: 210px; }
  .booking {
    position: absolute;
    left: 0;
    right: 0;
    bottom: 0;
    height: 56px;
    line-height: 56px;
    padding-left: 38px;
    color: var(--white);
    font-size: 25px;
    font-weight: 600;
    letter-spacing: 1.2px;
    white-space: nowrap;
  }
  .booking .divider { margin: 0 8px 0 14px; font-weight: 400; }
</style>
</head>
<body>
  <div class="sign">
    <svg class="sign-art" viewBox="0 0 1120 430">
      <defs>
        <linearGradient id="couple-tones" x1="0" y1="0" x2="1" y2="0">
          <stop offset="0" stop-color="#7d9a4a"/>
          <stop offset="0.35" stop-color="#d9b89a"/>
          <stop offset="0.7" stop-color="#e6d8cc"/>
          <stop offset="1" stop-color="#f1cfb4"/>
        </linearGradient>
        <linearGradient id="fade-to-orange" x1="0" y1="0" x2="1" y2="0">
          <stop offset="0" stop-color="#f1cfb4"/>
          <stop offset="1" stop-color="#f37022"/>
        </linearGradient>
        <radialGradient id="portrait-tones" cx="0.45" cy="0.45" r="0.6">
          <stop offset="0" stop-color="#8a8a8a"/>
          <stop offset="0.6" stop-color="#3a3a3a"/>
          <stop offset="1" stop-color="#111111"/>
        </radialGradient>
      </defs>

      <rect class="band-orange" x="0" y="0" width="1120" height="430" fill="var(--orange)"/>
      <rect class="photo-couple" x="0" y="0" width="330" height="290" fill="url(#couple-tones)" role="img" aria-label="Photo of a smiling older couple embracing outdoors"/>
      <rect class="photo-fade" x="330" y="0" width="260" height="290" fill="url(#fade-to-orange)"/>

      <path class="swoosh" d="M0,256 C260,258 470,226 585,122 C680,40 880,6 1120,0 L1120,18 C880,28 690,60 600,140 C480,250 260,285 0,282 Z" fill="var(--white)"/>
      <path class="panel-black" d="M0,282 C260,285 480,250 600,140 C690,60 880,28 1120,18 L1120,430 L0,430 Z" fill="var(--black)"/>

      <ellipse class="portrait-frame" cx="387" cy="245" rx="137" ry="82" fill="url(#portrait-tones)" stroke="var(--orange)" stroke-width="6" role="img" aria-label="Black and white photo of a pensive man"/>

      <rect class="band-booking" x="0" y="374" width="1120" height="56" fill="var(--orange)"/>
    </svg>

    <h1 class="title">Clinical<br>Hypnosis</h1>

    <ul class="services services-left">
      <li>Weight Loss</li>
      <li>Fear of Public Speaking</li>
      <li>Anxiety</li>
      <li>Depression</li>
    </ul>
    <ul class="services services-right">
      <li>PTS</li>
      <li>Stop Smoking</li>
      <li>Confidence Building</li>
      <li>Alcohol Moderation</li>
    </ul>

    <p class="booking">Book now: www.calmtidetrance.net.au<span class="divider">|</span>or call 9462 3089</p>
  </div>
</body>
</html>
```